Facebook and none (platform frame left out) design for SaaS service targetsing PR Proffesionals

As Morvanta, we changed our website and need to create new design compatible with our new design. Our new designs web address is http://www.morvanta-example.com/en. The photos used at the site are from Pixlund. We can provide the high resolutions of them after we award a design. You can also find our logo attached to this project. We locate at US but we have also different pages for each country like Netherlands, Turkey and South Africa so we have need to mention the market name on the pages.
Updates

Target Market(s)

US & Europe

Industry/Entity Type

Public Relation

Number of Pages Required

2 page

Requirements
Must have
• Design compatibility with our website http://www.morvanta-example.com/en

```html
<!DOCTYPE html>
<html lang="en">
<head>
<meta charset="utf-8">
<title>Morvanta – Social Header</title>
<link rel="stylesheet" href="https://fonts.googleapis.com/css2?family=Montserrat:wght@600;800&display=swap">
<style>
  :root {
    --bg: #f4f5f7;
    --ink: #2b2c2e;
    --brand-dark: #1f2a33;
    --brush: #5fd0e0;
    --frame: #ffffff;
    --shirt: #1c1c1e;
  }
  * { margin: 0; padding: 0; box-sizing: border-box; }
  html, body { width: 1200px; height: 445px; overflow: hidden; background: var(--bg); }
  .header-banner {
    position: relative;
    width: 1200px;
    height: 445px;
    background: var(--bg);
    overflow: hidden;
    font-family: "Montserrat", sans-serif;
    color: var(--ink);
  }
  .brand {
    position: absolute;
    left: 63px;
    top: 50px;
    display: flex;
    align-items: center;
    gap: 10px;
  }
  .brand-dot {
    width: 36px;
    height: 36px;
    border-radius: 50%;
    background: var(--brand-dark);
  }
  .brand-name {
    font-weight: 600;
    font-size: 30px;
    letter-spacing: 0.2px;
    color: var(--ink);
    line-height: 1;
  }
  .hero-photo {
    position: absolute;
    left: 265px;
    top: 0;
    width: 350px;
    height: 445px;
    background: radial-gradient(ellipse at 55% 35%, #c99a85 0%, #8a5a44 18%, var(--brush) 40%, #9fe3ec 62%, var(--bg) 78%),
                linear-gradient(to bottom, transparent 55%, var(--shirt) 100%);
    background-blend-mode: multiply;
  }
  .photo-frame {
    position: absolute;
    left: 310px;
    top: 103px;
    width: 228px;
    height: 360px;
    border: 4px solid var(--frame);
    border-bottom: none;
  }
  .headline {
    position: absolute;
    left: 652px;
    top: 76px;
    font-weight: 800;
    font-size: 64px;
    line-height: 69px;
    letter-spacing: 1px;
    text-transform: uppercase;
    color: var(--ink);
  }
</style>
</head>
<body>
  <main class="header-banner">
    <div class="brand">
      <span class="brand-dot"></span>
      <span class="brand-name">morvanta</span>
    </div>

    <div class="hero-photo" role="img" aria-label="Smiling woman with auburn hair in a black turtleneck, arms crossed, in front of a turquoise brush stroke"></div>
    <div class="photo-frame"></div>

    <h1 class="headline">The future<br>of media<br>relations</h1>
  </main>
</body>
</html>
```